Corporate Brightfen business cards to be handed to investor, bankers etc. Needs to have a young feel

I need business cards designed for a technology company that provides uber-like rapid response on the security industry. I would like it simple but very cool and tasteful. See attached documents for artwork and colours to be used. Cut sheet describes business model. Card stock should be thicker than normal. I would like the one side to be just the art and the other to have the contact info with maybe the pin somewhere.

Target Market(s)

Investors

Industry/Entity Type

Business

Contact Information for Business Card

Would like the logo attached on one side with name address and other info on the other side.

Font styles to use
Other font styles liked:
• See existing logo

Colors
6b449b
886aae
e4daeb
ffffff

Requirements
Must have
• Name: Dorian Felkatsis
• Address: 47 Larkfield Avenue, Toronto, On, M6K2B7
• Tel: 416-7291846
• Email: rolo@brightfen.io
Nice to have
• See logo colours

```html
<!DOCTYPE html>
<html lang="en">
<head>
<meta charset="utf-8">
<title>Brightfen Business Cards</title>
<link rel="stylesheet" href="https://fonts.googleapis.com/css2?family=Lato:wght@400;700&display=swap">
<style>
  :root {
    --brand-purple: #6b449b;
    --brand-purple-deep: #643f93;
    --brand-lilac: #886aae;
    --brand-mist: #e4daeb;
    --white: #ffffff;
    --text-grey: #8f8f8f;
    --canvas-bg: #d9d9dc;
  }
  * { box-sizing: border-box; margin: 0; padding: 0; }
  html, body {
    width: 1200px; height: 1000px; overflow: hidden;
    background: var(--canvas-bg);
    font-family: "Lato", Arial, sans-serif;
  }
  .canvas { position: relative; width: 1200px; height: 1000px; }

  .card {
    position: absolute; left: 270px; width: 662px; height: 379px;
    border-radius: 18px; overflow: hidden;
  }
  .card--front { top: 108px; background: var(--brand-purple); }
  .card--back { top: 521px; background: var(--white); }

  .front__halo {
    position: absolute; left: 612px; top: 100px;
    width: 300px; height: 300px; border-radius: 50%;
    background: var(--brand-purple-deep); opacity: 0.6;
    transform: translate(-50%, 0);
  }

  .wordmark {
    position: absolute; display: flex; align-items: center;
    color: var(--white); font-weight: 400; letter-spacing: -0.5px;
  }
  .wordmark__dot { border-radius: 50%; background: var(--white); }

  .front__wordmark { left: 0; right: 0; top: 136px; justify-content: center; font-size: 84px; line-height: 1; }
  .front__wordmark .wordmark__dot { width: 26px; height: 26px; margin-right: 16px; }

  .front__url {
    position: absolute; left: 0; right: 0; top: 330px;
    text-align: center; color: var(--white); font-size: 14px;
  }

  .back__disc {
    position: absolute; left: -178px; top: 0px;
    width: 522px; height: 522px; border-radius: 50%;
    background: var(--brand-purple);
  }
  .back__wordmark { left: 50px; top: 164px; font-size: 46px; line-height: 1; }
  .back__wordmark .wordmark__dot { width: 15px; height: 15px; margin-right: 9px; }

  .contact { position: absolute; left: 359px; top: 85px; right: 0; color: var(--text-grey); font-size: 17px; line-height: 22px; }
  .contact__name { color: var(--brand-purple); font-weight: 700; font-size: 22px; line-height: 28px; }
  .contact__role { margin-bottom: 16px; }
  .contact__rule { height: 1px; background: var(--brand-purple); margin-bottom: 17px; }
  .contact__address { margin-bottom: 9px; }
  .contact__label { color: var(--brand-purple); font-weight: 700; }
  .contact__accent { color: var(--brand-purple); }
</style>
</head>
<body>
<main class="canvas">
  <section class="card card--front" aria-label="Card front">
    <div class="front__halo"></div>
    <div class="wordmark front__wordmark"><span class="wordmark__dot"></span>brightfen</div>
    <p class="front__url">www.brightfen.io</p>
  </section>

  <section class="card card--back" aria-label="Card back">
    <div class="back__disc"></div>
    <div class="wordmark back__wordmark"><span class="wordmark__dot"></span>brightfen</div>
    <div class="contact">
      <p class="contact__name">Dorian Felkatsis</p>
      <p class="contact__role">President</p>
      <div class="contact__rule"></div>
      <p class="contact__address">47 Larkfield Avenue, Toronto,<br>On, M6K2B7</p>
      <p><span class="contact__label">T</span>: 416-7291846</p>
      <p><span class="contact__label">E</span>: rolo@brightfen.io</p>
      <p>www.<span class="contact__accent">brightfen</span>.io</p>
    </div>
  </section>
</main>
</body>
</html>
```